6 - 8 'Holistic' Instagram Graphics

Hi there!
We are looking to build up a library of Graphic Templates to use as Instagram & Facebook posts for our Holistic Medi Spa (& 3 other companies eventually)
This competition is for a sample of 6 - 8 designs. For the winner(s), we will make an agreement for a batch order (Looking for 200+ designs in total), and will be looking to make a long term arrangement.
Please find a full job description in the attached Word Document.
Any questions, don't hesitate to ask.
Thanks!
Medical Spa

```html
<!DOCTYPE html>
<html lang="en">
<head>
<meta charset="utf-8">
<title>LumaGrove – Free Treatment</title>
<link rel="stylesheet" href="https://fonts.googleapis.com/css2?family=Montserrat:wght@400;600;800&family=Open+Sans:wght@700&display=swap">
<style>
  :root {
    --coral: #ef8a78;
    --ink: #3a3536;
    --stone: #a8a699;
    --stone-btn: #b2b0a3;
    --teal: #93d5cd;
    --peach-dot: #f1cdb3;
    --paper: #ffffff;
  }
  * { margin: 0; padding: 0; box-sizing: border-box; }
  html, body { width: 1200px; height: 1200px; overflow: hidden; background: var(--paper); }
  .post { position: relative; width: 1200px; height: 1200px; background: var(--paper); overflow: hidden; font-family: "Montserrat", sans-serif; }
  .shapes { position: absolute; inset: 0; }
  .brand { position: absolute; left: 72px; top: 72px; display: flex; align-items: center; gap: 18px; }
  .brand-mark { width: 34px; height: 34px; border-radius: 50%; background: var(--stone); }
  .brand-text { color: var(--stone); font-weight: 400; }
  .brand-name { font-size: 54px; line-height: 1; letter-spacing: -0.5px; }
  .brand-tag { font-size: 20px; letter-spacing: 2px; margin-top: 6px; }
  .headline { position: absolute; left: 62px; top: 282px; color: var(--coral); font-weight: 800; line-height: 1; }
  .headline-free { display: block; font-size: 136px; letter-spacing: 2px; }
  .headline-treatment { display: block; font-size: 63px; margin-top: 26px; letter-spacing: 1px; }
  .offer { position: absolute; left: 72px; top: 515px; color: var(--ink); font-weight: 600; font-size: 58px; line-height: 73px; letter-spacing: 1.5px; }
  .site-button { position: absolute; left: 70px; top: 896px; width: 349px; height: 72px; border-radius: 12px; background: var(--stone-btn); color: var(--ink); font-family: "Open Sans", sans-serif; font-weight: 700; font-size: 26px; display: flex; align-items: center; justify-content: center; letter-spacing: 0.5px; }
</style>
</head>
<body>
<main class="post">
  <svg class="shapes" width="1200" height="1200" viewBox="0 0 1200 1200">
    <defs>
      <linearGradient id="photo-tone" x1="0" y1="0" x2="1" y2="1">
        <stop offset="0" stop-color="#e9d2cd"/>
        <stop offset="0.45" stop-color="#f3f0f4"/>
        <stop offset="0.8" stop-color="#d9c8ee"/>
        <stop offset="1" stop-color="#e6c6bd"/>
      </linearGradient>
    </defs>
    <path class="teal-wave" fill="var(--teal)" d="M0,1020 C55,1022 78,1045 68,1090 C55,1140 50,1175 110,1190 C150,1198 180,1200 205,1200 L0,1200 Z"/>
    <rect class="dot-band" role="img" aria-label="Small peach dot pattern" x="392" y="227" width="184" height="21" fill="var(--peach-dot)" opacity="0.5" rx="4"/>
    <rect class="dot-band" role="img" aria-label="Small peach dot pattern" x="64" y="801" width="189" height="26" fill="var(--peach-dot)" opacity="0.5" rx="4"/>
    <ellipse class="flower" role="img" aria-label="Line-drawn flower ornament" cx="834" cy="76" rx="68" ry="72" fill="#e8e6e0"/>
    <ellipse class="flower" role="img" aria-label="Line-drawn flower ornament" cx="527" cy="1027" rx="73" ry="80" fill="#e8e6e0"/>
    <path class="treatment-photo" role="img" aria-label="Photo of a gloved practitioner using a white body-contouring device on a client" fill="url(#photo-tone)" stroke="var(--coral)" stroke-width="5" d="M1203,330 C1120,270 1010,246 926,252 C680,272 500,420 506,600 C512,800 700,1050 936,1203 L1203,1203 Z"/>
  </svg>

  <div class="brand">
    <span class="brand-mark"></span>
    <div class="brand-text">
      <div class="brand-name">LumaGrove</div>
      <div class="brand-tag">HOLISTIC MEDI SPA</div>
    </div>
  </div>

  <h1 class="headline">
    <span class="headline-free">FREE</span>
    <span class="headline-treatment">TREATMENT</span>
  </h1>

  <p class="offer">when you<br>share post<br>with a friend</p>

  <div class="site-button">www.lumagrove.com</div>
</main>
</body>
</html>
```